I would like a minimalist clean and uncluttered website design.
Initially, I would like to see a front page only and would then like to build on the project front there.
RTV logo file with no background is attached, can be grey scale if the designer wishes.
I would like the front page to speak about the company's ethos and goals and I will need to put a great deal of thought into this to ensure it has the desired impact with the content on the subsequent pages.
The paragraph below gives a bit of an idea as to what this will include.
"RTV is a technology company providing approachable IT products and services to business:
With the overwhelming advancements in technology, businesses often find it difficult to determine what is available and what best suits their businesses specific needs.
We can assist business with their IT infrustucture, devices, software in procurement, installation, training, cost control as well as ongoing administration and support. We also keep our Clients informed of new technology and products which can benefit them"
Target Market(s)
Business, Health, Education, Professional Practices. Target age would be around 30 plus either male or female. Office administration level through Managing Directors. English speaking.

```html
<!DOCTYPE html>
<html lang="en">
<head>
<meta charset="utf-8">
<title>RTV – Approachable IT for Business</title>
<link href="https://fonts.googleapis.com/css2?family=Open+Sans:ital,wght@0,400;0,600;0,700;1,400;1,600;1,700&display=swap" rel="stylesheet">
<style>
:root{
  --green:#8cb43c;
  --navy:#2d5c8c;
  --ink:#333;
  --muted:#888;
  --line:#e3e3e3;
  --hero-bg:#f2f2f2;
  --footer-bg:#3a3a3a;
  --footer-text:#8c8c8c;
  --footer-head:#e6e6e6;
  --tag-bg:#555;
}
*{box-sizing:border-box;margin:0;padding:0}
html,body{width:1200px;height:2306px;overflow:hidden}
body{font-family:"Open Sans",Arial,sans-serif;color:var(--ink);background:#fff;position:relative}
.abs{position:absolute}

/* header */
.call{left:985px;top:40px;font-size:12px;color:var(--muted);display:flex;align-items:center;gap:8px}
.social{top:64px;display:flex;gap:4px}
.social span{width:33px;height:30px;background:#ccc;display:block}
.brand{left:42px;top:62px;display:flex;align-items:center;gap:12px}
.brand .mark{width:50px;height:50px;background:var(--green)}
.brand .name{font-size:42px;font-weight:600;color:var(--navy);letter-spacing:2px}
.nav{left:42px;top:155px;width:1116px;height:34px;border-top:1px solid var(--line);border-bottom:1px solid var(--line);display:flex;font-size:13px}
.nav a{display:flex;align-items:center;padding:0 24px;color:var(--ink);text-decoration:none;border-right:1px solid var(--line);letter-spacing:.3px}
.nav a.active{background:var(--navy);color:#fff;padding:0 26px}
.nav .search{margin-left:auto;border-left:1px solid var(--line);width:44px;display:flex;align-items:center;justify-content:center}

/* hero */
.hero{left:0;top:209px;width:1200px;height:387px;background:var(--hero-bg)}
.hero-brand{left:85px;top:392px}
.hero-brand .name{font-size:36px}
.hero-brand .mark{width:42px;height:42px}
.hero-quote{left:85px;top:483px;width:522px;background:var(--navy);color:#fff;font-style:italic;font-size:19px;line-height:23px;padding:4px 10px 6px;letter-spacing:.4px}
.hero-photo{left:635px;top:232px;width:472px;height:364px;background:linear-gradient(160deg,#d9d4cf 0%,#3a3a3a 55%,#1d1d22 100%)}

.tagline{left:42px;top:637px;width:1116px;text-align:center;font-style:italic;font-weight:700;font-size:25px;line-height:30px;color:#444;letter-spacing:.3px}

/* features */
.features{left:42px;top:743px;width:1116px;display:flex;gap:23px}
.feature{width:262px;height:240px;border:1px solid var(--line);text-align:center;padding-top:42px}
.feature svg{display:block;margin:0 auto}
.feature h3{font-weight:400;font-size:16px;letter-spacing:.5px;margin-top:32px}
.feature p{font-size:12.5px;line-height:19px;color:#999;margin:18px 30px 0}

.rule{left:42px;width:1116px;height:1px;background:var(--line)}

/* recent works */
.section-title{font-size:19px;font-weight:400;color:#444}
.arrows{left:1108px;top:1072px;display:flex;gap:3px}
.arrows span{width:22px;height:20px;background:#333;display:flex;align-items:center;justify-content:center}
.works{left:42px;top:1107px;width:1116px;display:flex;gap:23px}
.work{width:262px;text-align:center}
.work .thumb{height:147px}
.work h4{font-size:12.5px;font-weight:600;margin-top:24px;color:#333}
.work p{font-size:12.5px;color:#999;margin-top:5px}
.work .under{height:1px;background:var(--line);margin-top:24px}

/* queries */
.tabs{left:42px;top:1436px;display:flex;font-size:11.5px;letter-spacing:.5px}
.tabs span{height:33px;padding:0 18px;display:flex;align-items:center;border:1px solid var(--line);border-bottom:none;color:#999;background:#f7f7f7}
.tabs span.on{background:#fff;color:#333;border-top:2px solid var(--navy)}
.tab-panel{left:42px;top:1468px;width:740px;height:142px;border:1px solid var(--line);padding:20px 24px}
.tab-panel h3{font-size:21px;font-weight:600;letter-spacing:.3px}
.tab-panel p{font-size:12.5px;line-height:20px;color:#999;margin-top:10px}
.quote-card{left:802px;top:1435px;width:356px;height:144px;border:1px solid var(--line);padding:20px 20px;font-size:12.5px;line-height:19px;color:var(--navy)}
.quote-who{left:906px;top:1585px;font-size:12.5px;font-weight:700;color:#333}
.quote-who em{font-style:normal;font-weight:400;color:var(--navy)}

/* clients */
.clients-title{left:30px;top:1646px;font-size:29px;font-weight:600;color:#333}
.clients{left:42px;top:1780px;width:1116px;display:flex;justify-content:space-between;padding:0 24px}
.client{display:flex;align-items:center;gap:8px;font-size:26px;font-weight:400;color:#555}
.client i{width:18px;height:18px;background:#888;display:block;border-radius:50%}

/* footer */
.footer{left:0;top:1932px;width:1200px;height:374px;background:var(--footer-bg)}
.fcol{top:1966px;width:260px}
.fcol h5{font-size:14.5px;font-weight:400;color:var(--footer-head);margin-bottom:18px}
.fcol p{font-size:12.5px;line-height:19px;color:var(--footer-text);margin-bottom:14px}
.posts li{list-style:none;font-size:12.5px;color:var(--footer-text);margin-bottom:11px}
.posts li::before{content:"›";margin-right:8px}
.posts li small{display:block;font-style:italic;font-size:11px;padding-left:16px;margin-top:1px}
.tags{display:flex;flex-wrap:wrap;gap:4px;width:250px}
.tags span{background:var(--tag-bg);color:#ccc;font-size:12px;padding:4px 6px}
.fsocial{display:flex;gap:3px}
.fsocial span{width:36px;height:30px;background:#555;display:block}
.stream{display:grid;grid-template-columns:repeat(3,78px);gap:12px 14px}
.stream span{height:62px;background:linear-gradient(135deg,#e9e9e9,#777);display:block}
.fline{left:42px;top:2225px;width:1116px;height:1px;background:#4a4a4a}
.copyright{left:42px;top:2250px;font-size:11px;color:var(--footer-text)}
</style>
</head>
<body>

<header>
  <div class="abs call">
    <svg width="12" height="12" viewBox="0 0 24 24"><path fill="#333" d="M6.6 10.8a15 15 0 0 0 6.6 6.6l2.2-2.2a1 1 0 0 1 1-.2 11 11 0 0 0 3.6.6 1 1 0 0 1 1 1V20a1 1 0 0 1-1 1A17 17 0 0 1 3 4a1 1 0 0 1 1-1h3.5a1 1 0 0 1 1 1c0 1.3.2 2.5.6 3.6a1 1 0 0 1-.3 1z"/></svg>
    <span>Call Us : +00 1234567</span>
  </div>
  <div class="abs social" style="left:926px" aria-label="Social links">
    <span></span><span></span><span></span><span></span><span></span><span></span>
  </div>
  <div class="abs brand"><span class="mark"></span><span class="name">RTV</span></div>
  <nav class="abs nav">
    <a class="active">HOME</a><a>ABOUT US</a><a>SERVICES</a><a>OUR PRODUCTS</a><a>TESTIMONIALS</a><a>CONTACT</a>
    <span class="search"><svg width="14" height="14" viewBox="0 0 24 24"><circle cx="10" cy="10" r="6.5" fill="none" stroke="#aaa" stroke-width="2.5"/><path d="M15 15l6 6" stroke="#aaa" stroke-width="2.5"/></svg></span>
  </nav>
</header>

<section>
  <div class="abs hero"></div>
  <div class="abs brand hero-brand"><span class="mark"></span><span class="name">RTV</span></div>
  <p class="abs hero-quote">"We can assist business with their IT infrustucture, devices, software in procurement, installation, training, cost control as well as ongoing administration and support."</p>
  <div class="abs hero-photo" role="img" aria-label="Photo of two smiling business people in dark suits"></div>
</section>

<h2 class="abs tagline">"RTV is a technology company providing approachable IT products and services to business."</h2>

<section class="abs features">
  <div class="feature">
    <svg width="36" height="28" viewBox="0 0 36 28"><path d="M4 26L18 3l14 23" fill="none" stroke="#444" stroke-width="3"/><path d="M9 18h18" stroke="#444" stroke-width="3"/></svg>
    <h3>ABOUT US</h3>
    <p>Aliquam hendrit rutrum iaculis nullam ondimentum maluada velit beum donec sit amet</p>
  </div>
  <div class="feature">
    <svg width="36" height="28" viewBox="0 0 36 28"><path d="M3 7h7l14 14h7M3 21h7l14-14h7" fill="none" stroke="#444" stroke-width="3"/><path d="M28 2l5 5-5 5M28 16l5 5-5 5" fill="none" stroke="#444" stroke-width="2.5"/></svg>
    <h3>OUR SERVICES</h3>
    <p>Aliquam hendrit rutrum iaculis nullam ondimentum maluada velit beum donec sit amet</p>
  </div>
  <div class="feature">
    <svg width="36" height="28" viewBox="0 0 36 28"><rect x="2" y="2" width="32" height="19" fill="none" stroke="#444" stroke-width="2.5"/><path d="M12 26h12M18 21v5" stroke="#444" stroke-width="2.5"/></svg>
    <h3>OUR PRODUCTS</h3>
    <p>Aliquam hendrit rutrum iaculis nullam ondimentum maluada velit beum donec sit amet</p>
  </div>
  <div class="feature">
    <svg width="36" height="28" viewBox="0 0 36 28"><circle cx="14" cy="11" r="8" fill="none" stroke="#444" stroke-width="3"/><path d="M20 17l8 9" stroke="#444" stroke-width="4"/></svg>
    <h3>WHY CHOOSE US ?</h3>
    <p>Aliquam hendrit rutrum iaculis nullam ondimentum maluada velit beum donec sit amet</p>
  </div>
</section>

<div class="abs rule" style="top:1028px"></div>

<section>
  <h2 class="abs section-title" style="left:42px;top:1064px">Recent Works</h2>
  <div class="abs arrows">
    <span><svg width="8" height="10" viewBox="0 0 8 10"><path d="M6 1L2 5l4 4" fill="none" stroke="#fff" stroke-width="1.6"/></svg></span>
    <span><svg width="8" height="10" viewBox="0 0 8 10"><path d="M2 1l4 4-4 4" fill="none" stroke="#fff" stroke-width="1.6"/></svg></span>
  </div>
  <div class="abs works">
    <div class="work"><div class="thumb" role="img" aria-label="Grey photo of a hand holding a glowing globe" style="background:linear-gradient(180deg,#3c3c3c,#bdbdbd)"></div><h4>Your World</h4><p>Graphik Design / Print Design</p><div class="under"></div></div>
    <div class="work"><div class="thumb" role="img" aria-label="Grey photo of a man looking through binoculars" style="background:linear-gradient(180deg,#e6e6e6,#4a4a4a)"></div><h4>Man With Binoculars</h4><p>Graphik Design / Print Design</p><div class="under"></div></div>
    <div class="work"><div class="thumb" role="img" aria-label="Grey photo of a road running towards mountains" style="background:linear-gradient(180deg,#cfcfcf,#6a6a6a 55%,#2e2e2e)"></div><h4>Route Through the Mountains</h4><p>Graphik Design / Print Design</p><div class="under"></div></div>
    <div class="work"><div class="thumb" role="img" aria-label="Grey photo of spilled blueberries" style="background:linear-gradient(135deg,#9a9a9a,#2a2a2a)"></div><h4>Blueberries</h4><p>Graphik Design / Print Design</p><div class="under"></div></div>
  </div>
</section>

<section>
  <h2 class="abs section-title" style="left:42px;top:1392px">Queries</h2>
  <div class="abs tabs"><span class="on">CLEAN</span><span>EASY</span><span>SUPPORT</span></div>
  <div class="abs tab-panel">
    <h3>Unique &amp; Clean Design</h3>
    <p>Nulla sollicitudin tincidunt dui et egestas. Phasellus non sem elementum, ullamcorper metus vitae, accumsan dui. Duis dignissim condimentum lorem. Maecenas facilisis ipsum sed porttitor rutrum. Integer consequat semper elit sed viverra.</p>
  </div>
  <h2 class="abs section-title" style="left:802px;top:1392px">What Client's Say</h2>
  <blockquote class="abs quote-card">Lorem ipsum dolor sit amet, consectetur alpiscing elit. Nulla iaculis aliquet augue, varius purus sollicitudin eget. Donec tellus sollicitudin eu congue tempor dapibus et metus. Fusce ac ipsum at magna accumsan scelerisque sedon dolor.</blockquote>
  <p class="abs quote-who">Helen Marsh, <em>Manager</em></p>
</section>

<section>
  <h2 class="abs clients-title">Our Clients</h2>
  <div class="abs rule" style="top:1718px"></div>
  <div class="abs clients">
    <span class="client">Brightway</span>
    <span class="client">Vellum</span>
    <span class="client"><i></i>Orbitra</span>
    <span class="client">Cedarline</span>
    <span class="client"><i></i>Northpeak</span>
  </div>
</section>

<footer>
  <div class="abs footer"></div>
  <div class="abs fcol" style="left:42px">
    <h5>About Us</h5>
    <p>Risus mollis malesuada quis quis nulla. Vestibulum ante ipsum primis in faucibus orci luctus et ultrices posuere cubilia mattis vel elit porttitor euismod pharetra sem interdum.</p>
    <p>Etiam laoreet sagittis placerat magna sit amet massa posuere pretiumulum id est nulla, non adipiscing tortor.</p>
  </div>
  <div class="abs fcol" style="left:327px">
    <h5>Recent Posts</h5>
    <ul class="posts">
      <li>Single Clean Post<small>June 3, 2013</small></li>
      <li>Post With Custom Slideshow<small>June 3, 2013</small></li>
      <li>Video Post Format<small>June 3, 2013</small></li>
      <li>Post Without Image<small>June 3, 2013</small></li>
    </ul>
  </div>
  <div class="abs fcol" style="left:613px">
    <h5>Tag Cloud</h5>
    <div class="tags"><span>Audio</span><span>Design</span><span>Features</span><span>Logo</span><span>Photo</span><span>Photography</span><span>Video</span><span>Web</span></div>
    <h5 style="margin-top:40px">Social Links</h5>
    <div class="fsocial"><span></span><span></span><span></span><span></span><span></span><span></span></div>
  </div>
  <div class="abs fcol" style="left:898px">
    <h5>Photo Stream</h5>
    <div class="stream" role="img" aria-label="Thumbnails of website screenshots">
      <span></span><span></span><span></span><span></span><span></span><span></span>
    </div>
  </div>
  <div class="abs fline"></div>
  <p class="abs copyright">Copyright © 2013. RTV. All rights reserved</p>
</footer>

</body>
</html>
```